Webdesign mit Grundfarbe Weinrot für allgemeine Steuerberatung
Zielgruppe
Allgemeine Steuerberatung. Zielgruppe ist breit gefächert, allerdings soll die Webseite eher den Jungunternehmer ansprechen.
Aufgabenstellung
Die Grundfarbe sollte weinrot sein.

```html
<!DOCTYPE html>
<html lang="de">
<head>
<meta charset="utf-8">
<title>Steuerberatung Vorwerk</title>
<link href="https://fonts.googleapis.com/css2?family=Vollkorn:wght@400;500&family=Montserrat:wght@400;500;600&display=swap" rel="stylesheet">
<style>
:root{
  --wine:#5c0b27;
  --wine-dark:#470a1d;
  --footer:#5e1328;
  --accent:#b3173f;
  --ink:#3a2a2e;
  --text:#5d5659;
  --muted:#9a9497;
  --line:#e4e1e2;
  --soft:#f4f4f5;
  --white:#fff;
}
*{margin:0;padding:0;box-sizing:border-box}
html,body{width:1200px;height:2900px;overflow:hidden}
body{position:relative;background:var(--white);font-family:"Montserrat",sans-serif;color:var(--text)}
.abs{position:absolute}
.serif{font-family:"Vollkorn",serif;font-weight:400}

.topbar{left:0;top:0;width:1200px;height:30px;background:var(--wine);color:#f1dfe4;font-size:9.5px;display:flex;align-items:center;justify-content:flex-end;padding-right:95px;gap:30px}
.topbar span{display:flex;align-items:center;gap:8px}
.topbar .sep{width:1px;height:17px;background:#c99aa8}
.topbar b{font-weight:600}
.navbar{left:0;top:30px;width:1200px;height:55px;border-bottom:1px solid var(--line);background:var(--white)}
.nav{position:absolute;right:95px;top:22px;display:flex;gap:62px;font-size:10.5px;font-weight:500;letter-spacing:.6px;color:var(--ink)}
.brand{left:94px;top:0;width:118px;height:85px;background:var(--white);display:flex;flex-direction:column;align-items:center;justify-content:center;color:var(--wine);box-shadow:0 1px 4px rgba(0,0,0,.08)}
.brand .name{font-family:"Vollkorn",serif;font-size:19px;line-height:1}
.brand .sub{font-family:"Vollkorn",serif;font-size:13px;margin-top:5px}

.hero{left:0;top:85px;width:1200px;height:518px;background:linear-gradient(120deg,#3e3d42 0%,#6d6b6f 45%,#a9a7a9 70%,#5b5a5e 100%)}
.hero-text{left:243px;top:258px;color:var(--white)}
.hero-text h1{font-family:"Vollkorn",serif;font-weight:400;font-size:38px;letter-spacing:.3px}
.hero-text p{margin-top:22px;font-size:15px;line-height:23px;letter-spacing:.4px}
.btn-light{left:244px;top:405px;width:156px;height:38px;border-radius:19px;background:var(--white);color:var(--ink);font-size:11px;font-weight:600;letter-spacing:.5px;display:flex;align-items:center;justify-content:center}
.hero-edge{left:244px;top:603px;width:712px;height:12px;background:#f1f0f1}

.eyebrow{font-size:11.5px;color:var(--accent);letter-spacing:.5px}
.title{font-family:"Vollkorn",serif;font-size:30px;color:var(--ink);font-weight:400}
.rule{width:60px;height:3px;background:var(--accent)}

.about-text{left:244px;top:820px;width:352px;font-size:10.5px;line-height:19px}
.about-text p+p{margin-top:19px}
.photo{border-radius:3px}
.about-photo{left:609px;top:798px;width:347px;height:209px;background:linear-gradient(135deg,#d8d2cf,#8f8a88 55%,#3f4552);box-shadow:8px 8px 0 -1px #ececec}
.divider{left:244px;top:1101px;width:712px;height:1px;background:var(--line)}

.services{left:0;top:1102px;width:1200px;height:530px;background:linear-gradient(#fbfbfb,#ececee)}
.card{top:1324px;width:224px;height:215px;background:var(--white);border:1px solid var(--line);border-radius:3px}
.card .icon{position:absolute;left:12px;top:18px}
.card h3{position:absolute;left:70px;top:24px;font-family:"Vollkorn",serif;font-weight:400;font-size:17px;line-height:23px;color:var(--ink)}
.card ul{position:absolute;left:36px;top:90px;list-style:none;font-size:10px;line-height:19px;width:175px}
.card li{position:relative;padding-left:14px}
.card li:before{content:"";position:absolute;left:0;top:7px;width:4px;height:4px;background:var(--accent)}
.more{font-size:10px;font-weight:600;color:var(--accent);letter-spacing:.4px}
.card .more{position:absolute;left:36px;bottom:24px}
.card svg.arrow{position:absolute;right:20px;bottom:23px}

.news-img{top:1856px;width:225px;height:169px}
.img-office{background:linear-gradient(160deg,#e5e5e5,#9a9a9a 55%,#4a4a4a)}
.img-calc{background:linear-gradient(150deg,#f3f3f3,#cfcfcf 50%,#3a3a3a 75%,#b7343b)}
.news h3{position:absolute;top:2046px;width:225px;font-family:"Vollkorn",serif;font-weight:400;font-size:16.5px;line-height:22.5px;color:var(--wine)}
.news p{position:absolute;width:225px;font-size:10px;line-height:19px}
.news .date{position:absolute;top:2196px;font-size:9px;color:var(--muted)}
.news .more{position:absolute;top:2196px}
.news .base{position:absolute;top:2222px;width:232px;height:3px;background:#f0eeef}
.btn-all{left:521px;top:2273px;width:156px;height:37px;border-radius:19px;background:var(--accent);color:var(--white);font-size:11px;font-weight:600;letter-spacing:.5px;display:flex;align-items:center;justify-content:center}

.map{left:0;top:2403px;width:1200px;height:226px;background:linear-gradient(90deg,#f0f0f0,#e6e6e6 50%,#efefef)}
.footer{left:0;top:2629px;width:1200px;height:225px;background:var(--footer);color:#e6cfd6}
.footer h2{position:absolute;left:243px;top:44px;font-family:"Vollkorn",serif;font-weight:400;font-size:29px;color:var(--white)}
.footer .frule{position:absolute;left:244px;top:91px;width:712px;height:1px;background:#7e3a4c}
.footer .frule i{position:absolute;left:0;top:-1px;width:60px;height:3px;background:var(--accent)}
.fcol{position:absolute;top:135px;font-size:10.5px;line-height:19px}
.fcol h4{font-size:10.5px;font-weight:600;color:var(--white)}
.bottom{left:0;top:2854px;width:1200px;height:46px;background:var(--wine-dark);color:#e6cfd6;font-size:10.5px}
.bottom .links{position:absolute;left:244px;top:16px;display:flex;gap:40px;color:var(--white)}
.bottom .copy{position:absolute;right:244px;top:17px;font-size:9px;color:#b78d99}
</style>
</head>
<body>

<div class="abs topbar">
  <span><svg width="10" height="10" viewBox="0 0 10 10"><path d="M2 1l2 2-1 1.2c.6 1.2 1.6 2.2 2.8 2.8L7 6l2 2-1.4 1.4C4.5 9 1 5.5.6 2.4z" fill="#f1dfe4"/></svg>T: + 49 611-480273</span>
  <span><svg width="11" height="10" viewBox="0 0 11 10"><rect x="2" y="0" width="7" height="3" fill="#f1dfe4"/><rect x="0" y="3" width="11" height="5" rx="1" fill="#f1dfe4"/></svg>F: + 49 611-58216</span>
  <span><svg width="11" height="8" viewBox="0 0 11 8"><rect width="11" height="8" fill="#f1dfe4"/><path d="M0 0l5.5 4.5L11 0" stroke="#5c0b27" fill="none"/></svg>E: info@stbvorwerk.de</span>
  <i class="sep"></i>
  <span><svg width="11" height="11" viewBox="0 0 11 11"><circle cx="5.5" cy="5.5" r="4.5" stroke="#f1dfe4" fill="none"/><path d="M5.5 3v2.7L7.3 7" stroke="#f1dfe4" fill="none"/></svg><span><b>Mo - Do:</b> 08:00 - 16:00 Uhr</span></span>
  <span><b>Fr:</b> 08:00 - 12:30 Uhr</span>
</div>
<div class="abs navbar">
  <nav class="nav"><span>FÜR SELBSTÄNDIGE</span><span>FÜR ARBEITNEHMER</span><span>SONSTIGE EINKÜNFTE</span><span>AKTUELLES</span><span>KONTAKT</span></nav>
</div>
<div class="abs brand"><span class="name">Helene Vorwerk</span><span class="sub">Steuerberaterin</span></div>

<div class="abs hero" role="img" aria-label="Foto: Hände am Schreibtisch mit Taschenrechner und Unterlagen bei einer Beratung"></div>
<div class="abs hero-text">
  <h1>Lorem Ipsum dollor</h1>
  <p>DIPL. BETRIEBSWIRTIN (FH)<br>HELENE VORWERK STEUERBERATERIN</p>
</div>
<div class="abs btn-light">LEISTUNGEN</div>
<div class="abs hero-edge"></div>

<div class="abs eyebrow" style="left:244px;top:694px">ÜBER UNS</div>
<h2 class="abs title" style="left:243px;top:714px">Steuerberatung Vorwerk</h2>
<div class="abs rule" style="left:244px;top:773px"></div>
<div class="abs about-text">
  <p>Meine Kanzlei berät seit deren Gründung im Jahre 2003 Freiberufler, Gewerbetreibende, Kapitalgesellschaften, Personengesellschaften aus den verschiedensten Branchen sowie gemeinnützige Organisationen. Ebenso unterstützen wir gerne Existenzgründer und nebenberuflich Tätige, wie auch Arbeitnehmer, Vermieter und Rentner.</p>
  <p>Mein Team aus erfahrenen Steuerfachangestellten und ich freuen uns, Ihnen kompetent und individuell auf Ihre persönlichen Bedürfnisse abgestimmt, bei Ihren steuerlichen Angelegenheiten zu helfen!</p>
</div>
<div class="abs photo about-photo" role="img" aria-label="Teamfoto der Kanzleimitarbeiter in einem hellen Büro"></div>
<div class="abs divider"></div>

<div class="abs services" role="img" aria-label="Blasse Skyline als Hintergrund"></div>
<div class="abs eyebrow" style="left:244px;top:1195px">LOREM IPSUM</div>
<h2 class="abs title" style="left:243px;top:1215px">Leistungen</h2>
<div class="abs rule" style="left:244px;top:1273px"></div>

<div class="abs card" style="left:244px">
  <svg class="icon" width="44" height="42" viewBox="0 0 44 42" fill="none" stroke="#b3173f" stroke-width="1.3"><circle cx="8" cy="9" r="4"/><circle cx="22" cy="7" r="5"/><circle cx="36" cy="9" r="4"/><path d="M1 24c0-5 3-8 7-8s6 2 7 4M29 20c1-2 3-4 7-4s7 3 7 8"/><path d="M20 40V24a2 2 0 014 0v8l7 1c2 .4 3 2 2.5 4L32 40"/></svg>
  <h3>Gewerbe und<br>Existenzgründer</h3>
  <ul><li>Buchhaltung</li><li>Lohnabrechnungen</li><li>Jahresabschluss</li><li>Steuererklärungen</li></ul>
  <span class="more">MEHR</span>
  <svg class="arrow" width="12" height="9" viewBox="0 0 12 9" fill="none" stroke="#b3173f" stroke-width="1.2"><path d="M0 4.5h11M7 1l4 3.5L7 8"/></svg>
</div>
<div class="abs card" style="left:489px">
  <svg class="icon" width="44" height="42" viewBox="0 0 44 42" fill="none" stroke="#b3173f" stroke-width="1.3"><circle cx="22" cy="7" r="4"/><circle cx="7" cy="27" r="4"/><circle cx="37" cy="27" r="4"/><path d="M16 18c0-3 3-5 6-5s6 2 6 5M1 40c0-4 3-6 6-6s6 2 6 6M31 40c0-4 3-6 6-6s6 2 6 6M12 14l-4 6M32 14l4 6M15 31h14"/></svg>
  <h3>Leistungen für<br>Arbeitnehmer</h3>
  <ul><li>Lohnsteuerjahresausgleich</li><li>Veranlagung von Ehegatten und eingetragenen Lebenspartnerschaften</li></ul>
  <span class="more">MEHR</span>
  <svg class="arrow" width="12" height="9" viewBox="0 0 12 9" fill="none" stroke="#b3173f" stroke-width="1.2"><path d="M0 4.5h11M7 1l4 3.5L7 8"/></svg>
</div>
<div class="abs card" style="left:732px">
  <svg class="icon" width="44" height="42" viewBox="0 0 44 42" fill="none" stroke="#b3173f" stroke-width="1.3"><rect x="2" y="10" width="40" height="28" rx="3"/><path d="M15 10V5h14v5M2 20h40M18 18h8v6h-8z"/></svg>
  <h3 style="top:34px">Sonstige Einkünfte</h3>
  <ul><li>Rentner und Pensionäre</li><li>Vermieter</li></ul>
  <span class="more">MEHR</span>
  <svg class="arrow" width="12" height="9" viewBox="0 0 12 9" fill="none" stroke="#b3173f" stroke-width="1.2"><path d="M0 4.5h11M7 1l4 3.5L7 8"/></svg>
</div>

<div class="abs eyebrow" style="left:244px;top:1725px">NEWS &amp; BLOG</div>
<h2 class="abs title" style="left:243px;top:1745px">Aktuelle Meldungen</h2>
<div class="abs rule" style="left:244px;top:1803px"></div>

<div class="news">
  <div class="abs photo news-img img-office" style="left:244px" role="img" aria-label="Foto: Großraumbüro mit Mitarbeitenden an Schreibtischen"></div>
  <h3 style="left:243px">Lohnsteuer: Aktuelles zum Dienstwagen</h3>
  <p style="left:243px;top:2103px">Die Privatnutzung von Dienstwagen ist für viele Arbeitnehmer ein attraktiver Lohnbe­standteil, obgleich sich dieser Vorteil in aller Regel...</p>
  <span class="date" style="left:243px">08.10.2018</span>
  <span class="more" style="left:414px">MEHR</span>
  <svg class="abs" style="left:456px;top:2199px" width="12" height="9" viewBox="0 0 12 9" fill="none" stroke="#b3173f" stroke-width="1.2"><path d="M0 4.5h11M7 1l4 3.5L7 8"/></svg>
  <div class="base" style="left:240px"></div>

  <div class="abs photo news-img img-calc" style="left:487px" role="img" aria-label="Foto: Hand tippt auf Taschenrechner neben Diagrammen und Brille"></div>
  <h3 style="left:487px">Abschreibung bei „Arbeitswohnung“ im Miteigentum eines Ehepaars</h3>
  <p style="left:487px;top:2122px">Dienstwagen ist für viele Arbeitnehmer ein attraktiver Lohnbestandteil, obgleich sich dieser Vorteil in aller Regel...</p>
  <span class="date" style="left:487px">08.10.2018</span>
  <span class="more" style="left:658px">MEHR</span>
  <svg class="abs" style="left:700px;top:2199px" width="12" height="9" viewBox="0 0 12 9" fill="none" stroke="#b3173f" stroke-width="1.2"><path d="M0 4.5h11M7 1l4 3.5L7 8"/></svg>
  <div class="base" style="left:484px"></div>

  <div class="abs photo news-img img-office" style="left:731px" role="img" aria-label="Foto: Großraumbüro mit Mitarbeitenden an Schreibtischen"></div>
  <h3 style="left:730px">Kein Lohnzufluss bei Gehaltsumwandlung für vorzeitigen Ruhestand</h3>
  <p style="left:730px;top:2122px">Die Privatnutzung von Dienstwagen ist für viele Arbeitnehmer ein attraktiver Lohnbe­standteil, obgleich..</p>
  <span class="date" style="left:730px">08.10.2018</span>
  <span class="more" style="left:901px">MEHR</span>
  <svg class="abs" style="left:943px;top:2199px" width="12" height="9" viewBox="0 0 12 9" fill="none" stroke="#b3173f" stroke-width="1.2"><path d="M0 4.5h11M7 1l4 3.5L7 8"/></svg>
  <div class="base" style="left:727px"></div>
</div>

<div class="abs btn-all">ALLE AKTUELLES</div>

<div class="abs map" role="img" aria-label="Karte der Umgebung mit Standortmarkierung der Kanzlei"></div>
<svg class="abs" style="left:538px;top:2506px" width="24" height="32" viewBox="0 0 24 32"><path d="M12 0C5.4 0 0 5.2 0 11.6 0 20 12 32 12 32s12-12 12-20.4C24 5.2 18.6 0 12 0z" fill="#5c0b27"/><circle cx="12" cy="11.5" r="4.5" fill="#fff"/></svg>

<div class="abs footer">
  <h2>Kontakt</h2>
  <div class="frule"><i></i></div>
  <div class="fcol" style="left:244px"><h4>Addresse</h4>Lindenauer Str. 17<br>35217 Talbrück</div>
  <div class="fcol" style="left:426px"><h4>Telefon/Telefax</h4>T: + 49 611-480273<br>F: + 49 611-58216</div>
  <div class="fcol" style="left:609px"><h4>Email</h4>E: info@stbvorwerk.de</div>
  <div class="fcol" style="left:792px"><h4>Öffnungszeiten</h4><b>Mo-Do:</b>&nbsp; 08:00 - 16:00 Uhr<br><b>Fr:</b>&nbsp; 08:00 - 12:30 Uhr</div>
</div>
<div class="abs bottom">
  <div class="links"><span>Kontakt</span><span>Impressum</span><span>Datenschutz</span></div>
  <div class="copy">© 2019 Alle Rechte vorbehalten.. vorwerk-steuerberatung</div>
</div>

</body>
</html>
```